Shopify store for hemp

I need a store designed for Shopify for my hemp company. I currently have a brick and mortar store, but we are looking to get some business online as well. I will upload our logo for reference. We want a clean look. Categories like THCA Flower, Concentrates, Vapes, Edibles would be nice so that we can put individual products under them. I want something about all products being third-party lab tested. All products are sourced in the United States.
Updates

Need extra days to review

Target Market(s)

Former customers who live in different areas and signed up for our marketing list.

Industry/Entity Type

Hemp/Cannabis

Coding

Coded - Design and coding required

Number of Pages Required

1 page

Requirements
Must have
• Clean feel

```html
<!DOCTYPE html>
<html lang="en">
<head>
<meta charset="utf-8">
<title>Cedar Peak Dispensary — Home</title>
<link href="https://fonts.googleapis.com/css2?family=Arimo:wght@400;700&family=Source+Sans+3:wght@400;600&display=swap" rel="stylesheet">
<style>
  :root {
    --backdrop: #4b504d;
    --white: #ffffff;
    --leaf: #5c9e64;
    --leaf-deep: #1f5d3b;
    --ink: #111a14;
    --mist: #eef6f8;
    --sky-top: #e9e2d6;
    --ridge: #5f7f73;
    --canopy: #4f8a2c;
    --canopy-deep: #2f5e1f;
    --badge-blue: #2f9bc4;
  }
  * { box-sizing: border-box; margin: 0; padding: 0; }
  html, body { width: 986px; height: 1200px; overflow: hidden; }
  body { background: var(--backdrop); font-family: "Arimo", Arial, sans-serif; position: relative; }

  .page {
    position: absolute; left: 66px; top: 66px; width: 853px; height: 1067px;
    background: var(--white); overflow: hidden;
    box-shadow: 0 4px 18px rgba(0,0,0,.35);
  }

  /* Hero */
  .hero { position: absolute; left: 0; top: 0; width: 853px; height: 455px; }
  .hero-photo {
    position: absolute; inset: 0;
    background:
      radial-gradient(ellipse 260px 140px at 430px 150px, rgba(255,250,235,.55), transparent 70%),
      linear-gradient(180deg, var(--sky-top) 0%, #c9cfcb 14%, var(--ridge) 30%, #6e8f6a 45%, var(--canopy) 62%, var(--canopy-deep) 100%);
  }
  .hero-edge { position: absolute; left: 0; bottom: 0; width: 853px; height: 45px; }

  .nav {
    position: absolute; left: 223px; top: 31px; width: 407px; height: 28px;
    background: var(--leaf); border-radius: 14px;
    display: flex; align-items: center; justify-content: space-between; padding: 0 22px 0 18px;
  }
  .nav-group { display: flex; gap: 17px; }
  .nav a { color: var(--white); text-decoration: none; font-weight: 700; font-size: 9.5px; }
  .brand {
    position: absolute; left: 390px; top: 7px; width: 74px; height: 74px; border-radius: 50%;
    background: var(--white); border: 3px solid var(--leaf);
    display: flex; align-items: center; justify-content: center; text-align: center;
    color: var(--leaf-deep); font-weight: 700; font-size: 9px; line-height: 1.15; padding: 8px;
  }

  .hero-title {
    position: absolute; left: 0; width: 853px; top: 147px; text-align: center;
    color: var(--white); font-size: 33px; font-weight: 700; letter-spacing: -.2px;
    text-shadow: 0 1px 3px rgba(0,0,0,.25);
  }
  .hero-sub {
    position: absolute; left: 0; width: 853px; top: 198px; text-align: center;
    color: var(--white); font-size: 14.5px; font-weight: 700;
    text-shadow: 0 1px 3px rgba(0,0,0,.3);
  }
  .btn-hero {
    position: absolute; left: 365px; top: 233px; width: 124px; height: 34px; border-radius: 17px;
    background: var(--leaf); color: var(--white); font-weight: 700; font-size: 15px;
    display: flex; align-items: center; justify-content: center; text-decoration: none;
  }
  .seal {
    position: absolute; left: 397px; top: 404px; width: 60px; height: 60px; border-radius: 50%;
    background: var(--white); border: 3px solid var(--leaf);
  }

  /* Categories */
  .section-title {
    position: absolute; left: 0; width: 853px; top: 501px; text-align: center;
    color: var(--leaf); font-size: 31px; font-weight: 700;
  }
  .categories { position: absolute; left: 125px; top: 557px; display: flex; gap: 12px; }
  .category { width: 142px; height: 204px; background: var(--mist); text-align: center; }
  .category-photo { height: 104px; position: relative; }
  .category-photo::after { content: ""; position: absolute; inset: 4px; border: 1px solid rgba(255,255,255,.85); }
  .photo-flower { background: linear-gradient(135deg, #4f4a3e, #8a8672 50%, #3e3a30); }
  .photo-concentrate { background: linear-gradient(135deg, #e0a236, #c77a12 55%, #f0b44a); }
  .photo-vape { background: linear-gradient(120deg, #3a2c6e, #c42a8e 45%, #1b6fb5 75%, #222); }
  .photo-edible { background: linear-gradient(135deg, #5d6a3c, #b8563a 45%, #d89b3f 70%, #4d3322); }
  .category-icon { display: block; margin: 11px auto 0; width: 30px; height: 30px; }
  .category-name { font-size: 11px; font-weight: 700; color: var(--ink); margin-top: 7px; }
  .category-text { font-size: 7.6px; line-height: 12px; color: var(--ink); margin-top: 5px; padding: 0 10px; }

  /* About */
  .about { position: absolute; left: 0; top: 817px; width: 853px; height: 222px; background: var(--mist); }
  .about-photo {
    position: absolute; left: 0; top: 0; width: 427px; height: 222px;
    background:
      radial-gradient(ellipse 140px 120px at 60px 80px, rgba(255,220,150,.7), transparent 70%),
      linear-gradient(135deg, #e3a45a, #b86c2c 50%, #7a4522);
  }
  .about-badge {
    position: absolute; left: 356px; top: 39px; width: 144px; height: 144px; border-radius: 50%;
    background: var(--white); border: 4px solid var(--badge-blue);
  }
  .about-body { position: absolute; left: 537px; top: 46px; width: 280px; font-family: "Source Sans 3", Arial, sans-serif; }
  .about-title { font-family: "Arimo", Arial, sans-serif; font-size: 25px; font-weight: 700; color: var(--leaf-deep); line-height: 1.1; }
  .about-text { font-size: 7.6px; line-height: 11.3px; color: var(--ink); margin-top: 10px; }
  .about-text + .about-text { margin-top: 11px; }
  .btn-about {
    display: inline-flex; align-items: center; justify-content: center; margin-top: 14px;
    width: 75px; height: 20px; border-radius: 10px; background: var(--leaf-deep);
    color: var(--white); font-family: "Arimo", Arial, sans-serif; font-weight: 700; font-size: 9px; text-decoration: none;
  }

  .footer {
    position: absolute; left: 0; top: 1039px; width: 853px; height: 28px; background: var(--leaf);
    color: var(--white); font-family: "Source Sans 3", Arial, sans-serif; font-size: 7.6px;
    display: flex; align-items: center; justify-content: center;
  }
</style>
</head>
<body>
<main class="page">
  <header class="hero">
    <div class="hero-photo" role="img" aria-label="Misty mountain valley at sunrise with a field of green hemp plants in the foreground"></div>
    <svg class="hero-edge" viewBox="0 0 853 45" preserveAspectRatio="none" aria-hidden="true">
      <polygon fill="#ffffff" points="0,37 12,32 30,30 43,42 56,30 80,29 101,45 118,28 150,31 165,22 187,34 210,27 240,30 268,38 289,28 310,36 330,26 360,40 380,28 400,22 430,22 470,24 500,20 530,10 560,25 575,21 600,30 612,31 622,26 640,22 660,36 685,24 700,28 718,23 735,38 750,27 765,30 790,38 810,27 830,30 853,20 853,45 0,45"/>
    </svg>

    <nav class="nav">
      <div class="nav-group"><a href="#">THCA Flower</a><a href="#">Concentrates</a></div>
      <div class="nav-group"><a href="#">Vapes</a><a href="#">Edibles</a><a href="#">Contact</a></div>
    </nav>
    <div class="brand">Cedar Peak Dispensary</div>

    <h1 class="hero-title">Welcome to Cedar Peak Dispensary</h1>
    <p class="hero-sub">Clean, natural hemp products delivered with care.</p>
    <a class="btn-hero" href="#">SHOP NOW</a>
    <div class="seal" role="img" aria-label="Lab tested badge"></div>
  </header>

  <h2 class="section-title">Shop by Category</h2>
  <section class="categories">
    <article class="category">
      <div class="category-photo photo-flower" role="img" aria-label="Close-up of dried hemp flower buds"></div>
      <svg class="category-icon" viewBox="0 0 30 30" fill="none" stroke="#1f5d3b" stroke-width="1.3" aria-hidden="true">
        <path d="M15 4 C18 8 18 13 15 17 C12 13 12 8 15 4Z"/><path d="M4 11 C9 11 13 14 15 17 C10 18 6 15 4 11Z"/><path d="M26 11 C21 11 17 14 15 17 C20 18 24 15 26 11Z"/><path d="M15 17 V26"/><path d="M12 26 H18"/>
      </svg>
      <h3 class="category-name">THCA Flower</h3>
      <p class="category-text">Premium hemp flower carefully sourced for quality.</p>
    </article>
    <article class="category">
      <div class="category-photo photo-concentrate" role="img" aria-label="Close-up of amber hemp concentrate"></div>
      <svg class="category-icon" viewBox="0 0 30 30" fill="none" stroke="#1f5d3b" stroke-width="1.3" aria-hidden="true">
        <circle cx="15" cy="15" r="11"/><circle cx="15" cy="15" r="6"/><circle cx="15" cy="15" r="1.8" fill="#1f5d3b"/>
        <circle cx="15" cy="4" r="1.3" fill="#1f5d3b"/><circle cx="15" cy="26" r="1.3" fill="#1f5d3b"/><circle cx="4" cy="15" r="1.3" fill="#1f5d3b"/><circle cx="26" cy="15" r="1.3" fill="#1f5d3b"/>
      </svg>
      <h3 class="category-name">Concentrates</h3>
      <p class="category-text">High-potency hemp concentrates for every preference.</p>
    </article>
    <article class="category">
      <div class="category-photo photo-vape" role="img" aria-label="Assorted colourful vape pens and devices"></div>
      <svg class="category-icon" viewBox="0 0 30 30" fill="none" stroke="#1f5d3b" stroke-width="1.3" aria-hidden="true">
        <rect x="6" y="9" width="8" height="18" rx="1.5"/><rect x="8" y="4" width="4" height="5"/><rect x="16" y="13" width="8" height="14" rx="1.5"/><rect x="18" y="9" width="4" height="4"/><path d="M10 15 V21"/>
      </svg>
      <h3 class="category-name">Vapes</h3>
      <p class="category-text">Smooth and flavorful vape cartridges and pens.</p>
    </article>
    <article class="category">
      <div class="category-photo photo-edible" role="img" aria-label="Colourful hemp gummies on a wooden board"></div>
      <svg class="category-icon" viewBox="0 0 30 30" fill="none" stroke="#1f5d3b" stroke-width="1.3" aria-hidden="true">
        <rect x="4" y="8" width="16" height="19" rx="2"/><path d="M4 12 H20"/><circle cx="22" cy="8" r="5"/>
        <circle cx="9" cy="18" r="2"/><circle cx="15" cy="18" r="2"/><circle cx="9" cy="23" r="2"/><circle cx="15" cy="23" r="2"/>
      </svg>
      <h3 class="category-name">Edibles</h3>
      <p class="category-text">Delicious hemp-infused gummies, chocolates, and more.</p>
    </article>
  </section>

  <section class="about">
    <div class="about-photo" role="img" aria-label="Two shop staff chatting in a warm, sunlit dispensary with stocked shelves"></div>
    <div class="about-badge" role="img" aria-label="Lab tested badge"></div>
    <div class="about-body">
      <h2 class="about-title">About Us</h2>
      <p class="about-text">Cedar Peak Dispensary brings our trusted brick &amp; mortar experience online. We’re committed to clean, natural hemp products for wellness and enjoyment.</p>
      <p class="about-text">All our products are third-party lab tested to ensure purity, safety, and consistency. Shop confidently knowing our products meet the highest standards.</p>
      <a class="btn-about" href="#">SHOP NOW</a>
    </div>
  </section>

  <footer class="footer">© 2025 Cedar Peak Dispensary. All rights reserved.</footer>
</main>
</body>
</html>
```